Dentist Seminar invite please see .doc in attachments

Need an 8.5 x 11 invite designed. It will be for an invitation to attend an evening seminar on dental procedures. Feel free to utilize both front and back ONLY IF REQUIRED

See Assets & PPT with additional assets.

INSPIRATION: FIle NAME KOLVEN

Target Market(s)

Dentists

Industry/Entity Type

Dental

Other font styles liked:
• lato, garamond, palatino linotype

Colors
cee9f5
9bcb3c
0492cd
cadf82

Requirements
Must have
• Must have the colours suggested, and professional feel.
• Some of the assets merged cleanly into the design
Should not have
• Any pictures of teeth, tooth brushes or any dental product

```html
<!DOCTYPE html>
<html lang="en">
<head>
<meta charset="utf-8">
<title>Digital Dentistry Evening Seminar – Invitation</title>
<link rel="stylesheet" href="https://fonts.googleapis.com/css2?family=Lato:wght@300;400;700;900&display=swap">
<style>
  :root{
    --stage:#e4e6e8;
    --paper-top:#ffffff;
    --paper-bottom:#d9dadc;
    --charcoal:#4d4e50;
    --ink:#333437;
    --ink-soft:#55575a;
    --accent-blue:#0492cd;
    --accent-green:#9bcb3c;
    --accent-lime:#cadf82;
    --accent-ice:#cee9f5;
    --on-dark:#ffffff;
  }
  *{box-sizing:border-box;margin:0;padding:0}
  html,body{width:1200px;height:776px;overflow:hidden;background:var(--stage)}
  body{font-family:"Lato",Arial,sans-serif;color:var(--ink);position:relative}

  .sheet{
    position:absolute;top:90px;width:460px;height:595px;overflow:hidden;
    background:linear-gradient(160deg,var(--paper-top) 30%,var(--paper-bottom) 100%);
    box-shadow:0 6px 18px rgba(0,0,0,.18);
  }
  .sheet--front{left:90px}
  .sheet--back{left:650px}
  .sheet__shapes{position:absolute;inset:0;width:460px;height:595px}

  .section-title{font-weight:700;font-size:13px;color:var(--ink);position:relative;padding-bottom:3px;display:inline-block}
  .section-title::after{content:"";position:absolute;left:0;bottom:0;width:100%;height:2px;background:var(--accent-blue)}

  .synopsis{position:absolute;left:30px;top:42px;width:285px}
  .synopsis__body,.biography__body{margin-top:8px;font-size:6.4px;line-height:8.2px;color:var(--ink-soft)}

  .objectives{position:absolute;left:30px;top:432px;width:345px}
  .objectives__title{font-size:13px;line-height:14px;font-weight:700;color:var(--ink)}
  .objectives__title span{display:inline-block;font-weight:300;font-size:15px;line-height:18px;position:relative;padding-bottom:2px}
  .objectives__title span::after{content:"";position:absolute;left:0;bottom:0;width:100%;height:2px;background:var(--accent-blue)}
  .objectives__list{list-style:none;margin-top:10px}
  .objectives__list li{position:relative;padding-left:12px;font-size:7.3px;line-height:8.8px;color:var(--ink-soft)}
  .objectives__list li::before{content:"";position:absolute;left:1px;top:3px;width:4px;height:4px;border-radius:50%;background:var(--accent-blue)}

  .biography{position:absolute;left:30px;top:50px;width:275px}

  .event-details{position:absolute;right:22px;top:350px;text-align:right;color:var(--on-dark);font-size:12.5px;line-height:15px}
  .event-details__venue{margin-top:22px}

  .registration{position:absolute;left:38px;top:468px}
  .registration__label{font-size:15px;font-weight:400;color:var(--ink-soft);display:inline-block;position:relative;padding-bottom:4px}
  .registration__label::after{content:"";position:absolute;left:0;bottom:0;width:100%;height:2px;background:var(--accent-blue)}
  .registration__email{margin-top:6px;font-size:26px;font-weight:400;color:var(--ink-soft);letter-spacing:-.2px}
  .registration__phone{font-size:38px;font-weight:900;color:var(--ink-soft);line-height:40px;letter-spacing:-.5px}
</style>
</head>
<body>

<!-- Front sheet -->
<section class="sheet sheet--front">
  <svg class="sheet__shapes" viewBox="0 0 460 595" aria-hidden="false">
    <defs>
      <linearGradient id="clinicalTone" x1="0" y1="0" x2="1" y2="0">
        <stop offset="0" stop-color="#3f7f9e"/>
        <stop offset=".35" stop-color="#7a3036"/>
        <stop offset=".7" stop-color="#b8454a"/>
        <stop offset="1" stop-color="#d9a79a"/>
      </linearGradient>
      <linearGradient id="guideTone" x1="0" y1="0" x2="1" y2="1">
        <stop offset="0" stop-color="#8fd0ad"/>
        <stop offset=".5" stop-color="#93307f"/>
        <stop offset="1" stop-color="#e8e4d6"/>
      </linearGradient>
    </defs>
    <polygon class="accent-wedge" points="300,0 460,0 460,90" fill="var(--accent-green)"/>
    <polygon class="accent-wedge-soft" points="300,0 380,0 460,90 460,110" fill="var(--accent-lime)" opacity=".0"/>
    <polygon points="0,340 460,110 460,300 245,440" fill="url(#clinicalTone)" role="img" aria-label="Clinical photograph of a dental implant being placed"/>
    <polygon class="charcoal-panel" points="245,440 460,300 460,470" fill="var(--charcoal)"/>
    <polygon points="330,395 440,355 445,420 360,440" fill="url(#guideTone)" role="img" aria-label="3D model of a printed surgical guide with implant drill paths"/>
  </svg>

  <div class="synopsis">
    <h2 class="section-title">Synopsis:</h2>
    <p class="synopsis__body">This presentation will cover the recent advances in digital technology and its use in dentistry. Digital protocols will be introduced that can improve upon traditional treatment planning approaches. The use of modern 3D technology and the digital workflow can simplify advanced procedures and enhance the predictability of surgical outcomes. Through state of the art imaging, intra-oral scanning, live guided navigation and 3D printing, multiple digital workflows and their surgical applications will be discussed through real clinical cases. This lecture will showcase the synergy between advanced technology and fundamental biological principles, and techniques that have never been seen before.</p>
  </div>

  <div class="objectives">
    <h2 class="objectives__title">Learning<br><span>Objectives:</span></h2>
    <ul class="objectives__list">
      <li>Discuss the use of modern digital technologies like CBCT, intra-oral scanning, and 3D printing.</li>
      <li>Learn to digitally plan surgical procedures and use 3D printed surgical guides</li>
      <li>Understand the benefits of microsurgery and the use of surgical operating microscope</li>
      <li>Understand the benefits of digital technology in surgical treatment planning</li>
      <li>Understanding and benefits of live guided navigation surgery and its applications</li>
      <li>Learn about innovative procedures like digitally guided bone block harvesting, digitally created bone grafts, and osteotomy guides.</li>
      <li>Understand how computer automated design software can improve upon real live surgery.</li>
    </ul>
  </div>
</section>

<!-- Back sheet -->
<section class="sheet sheet--back">
  <svg class="sheet__shapes" viewBox="0 0 460 595">
    <defs>
      <linearGradient id="jawTone" x1="0" y1="0" x2="1" y2="1">
        <stop offset="0" stop-color="#9b9c9e"/>
        <stop offset=".6" stop-color="#c3c4c6"/>
        <stop offset="1" stop-color="#8e8f91"/>
      </linearGradient>
      <linearGradient id="skullTone" x1="0" y1="0" x2="0" y2="1">
        <stop offset="0" stop-color="#f1ede0"/>
        <stop offset="1" stop-color="#d8d2c0"/>
      </linearGradient>
    </defs>
    <polygon class="accent-wedge" points="290,0 460,0 460,75" fill="var(--accent-green)"/>
    <polygon class="grey-panel" points="250,190 460,65 460,315 265,425" fill="#c9cacc"/>
    <polygon points="300,200 420,110 450,270 330,305" fill="url(#jawTone)" role="img" aria-label="3D render of a jaw model with colour-coded teeth and a planned implant"/>
    <polygon class="blue-panel" points="58,300 250,190 265,425" fill="var(--accent-blue)"/>
    <polygon points="105,285 205,265 210,325 125,330" fill="url(#skullTone)" role="img" aria-label="3D scan of an upper jaw and skull"/>
    <polygon class="charcoal-panel" points="265,425 460,305 460,595" fill="var(--charcoal)"/>
  </svg>

  <div class="biography">
    <h2 class="section-title">Biography</h2>
    <p class="biography__body">Dr. Naheed Kolven is a clinician and educator with a practice focused on implant and guided surgery. Over many years they have lectured widely on digital workflows, 3D planning and printed surgical guides, and have helped colleagues bring new technology into daily care with safe, predictable results for their patients.</p>
  </div>

  <div class="event-details">
    <p class="event-details__date">November 13, 2017<br>6:30 – 9:30pm</p>
    <p class="event-details__venue">Maple Hall Banquet Centre<br>48 Harwood St.<br>Toronto, Ontario<br>A1B 2C3</p>
  </div>

  <div class="registration">
    <h2 class="registration__label">Registration:</h2>
    <p class="registration__email">n.kolven@email.com</p>
    <p class="registration__phone">555-013-2478</p>
  </div>
</section>

</body>
</html>
```